Business Cards Needed For Veterinary Business

Looking for a business card design for a veterinary blood bank. We would like it to be clean and professional on appearance but still warm and inviting. We would like to utilize our logo and similar coloring. We will use our phone number, email, website, employee name, employee title.

We do not want a bunch of animated animal photos but do not need the style to be as clinical as a laboratory or human medical procedure office.

We are looking for some creative ideas to choose from so that we can generate a standout professional business card for our management team to utilize.

Target Market(s)

professionals

Industry/Entity Type

veterinary

Contact Information for Business Card

employee name, employee title, phone number, website URL, email

Font styles to use
Sans Serif

Colors
0054AA
0677BA
7BADD7
CADEEF
E8F1F8
EB3D1F
EC4F4E
F09395
F8D3D4
FCEDEE

Requirements
Nice to have
• creative design
Should not have
• animated photos

```html
<!DOCTYPE html>
<html lang="en">
<head>
<meta charset="utf-8">
<title>Northfield Animal Blood Service – Business Card</title>
<link href="https://fonts.googleapis.com/css2?family=Open+Sans:wght@400;600;700&display=swap" rel="stylesheet">
<style>
  :root {
    --backdrop: #232323;
    --card: #1c1d1c;
    --red: #ec2227;
    --blue: #0054aa;
    --white: #ffffff;
  }
  * { box-sizing: border-box; margin: 0; padding: 0; }
  html, body {
    width: 1200px; height: 711px; overflow: hidden;
    background: var(--backdrop);
    font-family: "Open Sans", Arial, sans-serif;
  }
  .stage { position: relative; width: 1200px; height: 711px; }
  .card {
    position: absolute;
    top: 207px;
    width: 520px; height: 297px;
    background: var(--card);
    border: 1.5px solid var(--red);
    overflow: hidden;
  }
  .card--front { left: 40px; }
  .card--back { left: 640px; }

  .brand {
    position: absolute;
    display: flex; align-items: center; gap: 10px;
    white-space: nowrap;
  }
  .brand__dot {
    border-radius: 50%;
    background: var(--red); flex: none;
  }
  .brand__name {
    color: var(--red);
    font-weight: 700;
    line-height: 1.1;
    text-transform: uppercase;
    white-space: nowrap;
  }
  .card--front .brand { left: 50%; top: 50%; transform: translate(-50%, -50%); gap: 14px; }
  .card--front .brand__dot { width: 46px; height: 46px; }
  .card--front .brand__name { font-size: 28px; }

  .card--back .brand { left: 26px; top: 50%; transform: translateY(-50%); }
  .card--back .brand__dot { width: 30px; height: 30px; }
  .card--back .brand__name { font-size: 14px; }

  .divider {
    position: absolute; left: 268px; top: 55px;
    width: 1.5px; height: 190px; background: var(--red);
  }
  .details {
    position: absolute; left: 292px; top: 62px;
    color: var(--white);
    white-space: nowrap;
  }
  .person__name { font-size: 22px; font-weight: 700; line-height: 1.1; }
  .person__first { color: var(--red); }
  .person__last { color: var(--blue); }
  .person__title { font-size: 12px; font-weight: 600; margin-top: 3px; }
  .address { font-size: 12px; line-height: 1.45; margin-top: 16px; }
  .contact { list-style: none; margin-top: 14px; font-size: 12px; }
  .contact li { display: flex; align-items: center; gap: 8px; line-height: 1.7; }
  .contact svg { width: 12px; height: 12px; fill: var(--red); flex: none; }
</style>
</head>
<body>
<main class="stage">
  <section class="card card--front" aria-label="Card front">
    <div class="brand">
      <span class="brand__dot"></span>
      <span class="brand__name">Northfield<br>Animal Blood Service</span>
    </div>
  </section>

  <section class="card card--back" aria-label="Card back">
    <div class="brand">
      <span class="brand__dot"></span>
      <span class="brand__name">Northfield<br>Animal Blood Service</span>
    </div>
    <div class="divider"></div>
    <div class="details">
      <p class="person__name"><span class="person__first">Marta</span> <span class="person__last">Lindqvist</span></p>
      <p class="person__title">Managing Director</p>
      <p class="address">2217 Cedar Ave<br>Fairview, OH 45012</p>
      <ul class="contact">
        <li>
          <svg viewBox="0 0 24 24" aria-hidden="true"><path d="M6.6 10.8a15.5 15.5 0 0 0 6.6 6.6l2.2-2.2a1 1 0 0 1 1-.25 11.4 11.4 0 0 0 3.6.57 1 1 0 0 1 1 1V20a1 1 0 0 1-1 1A17 17 0 0 1 3 4a1 1 0 0 1 1-1h3.5a1 1 0 0 1 1 1c0 1.250.2 2.450.57 3.57a1 1 0 0 1-.25 1z"/></svg>
          (555) 014-2290
        </li>
        <li>
          <svg viewBox="0 0 24 24" aria-hidden="true"><path d="M12 2a10 10 0 1 0 0 20 10 10 0 0 0 0-20zm6.9 6h-2.9a15.7 15.7 0 0 0-1.4-3.6A8 8 0 0 1 18.9 8zM12 4a14 14 0 0 1 1.9 4h-3.8A14 14 0 0 1 12 4zM4.3 14a8 8 0 0 1 0-4h3.4a16.5 16.5 0 0 0 0 4zm.8 2h2.9a15.7 15.7 0 0 0 1.4 3.6A8 8 0 0 1 5.1 16zM8 8H5.1a8 8 0 0 1 4.3-3.6A15.7 15.7 0 0 0 8 8zm4 12a14 14 0 0 1-1.9-4h3.8A14 14 0 0 1 12 20zm2.3-6H9.7a14.7 14.7 0 0 1 0-4h4.6a14.7 14.7 0 0 1 0 4zm.3 5.6a15.7 15.7 0 0 0 1.4-3.6h2.9a8 8 0 0 1-4.3 3.6zm1.7-5.6a16.5 16.5 0 0 0 0-4h3.4a8 8 0 0 1 0 4z"/></svg>
          www.northfieldabs.com
        </li>
        <li>
          <svg viewBox="0 0 24 24" aria-hidden="true"><path d="M3 5h18a1 1 0 0 1 1 1v12a1 1 0 0 1-1 1H3a1 1 0 0 1-1-1V6a1 1 0 0 1 1-1zm9 7.2L4.5 7v10h15V7z"/></svg>
          donate@northfieldabs.com
        </li>
      </ul>
    </div>
  </section>
</main>
</body>
</html>
```